The Brightwater Compass Business Card

We need an attractive business card with the logo that we bought from ArtVantly last year.
Our mission is to contribute to change the way today's leaders manage business companies bringing value to the workplace and helping them to build a new model of creating wealth.
Our logo is clear about our values : we seek Positive Change through People and are convinced that the pursuit of individual well-being and the chase of economic results can converge with the right management.
Management Consulting
Corinne Fabrelle
+34 612 98 70 31
corinne.fabrelle@thebrightwatercompass-mail.net
www.thebrightwatercompass-mail.net

```html
<!DOCTYPE html>
<html lang="en">
<head>
<meta charset="utf-8">
<title>The Brightwater Compass – Business Card</title>
<link rel="stylesheet" href="https://fonts.googleapis.com/css2?family=Barlow:wght@400;500&display=swap">
<style>
  :root {
    --bg: #1e1f1f;
    --card-white: #f5f7f7;
    --ink-teal: #3c6e69;
    --teal-1: #3f9985;
    --teal-2: #5aa893;
    --teal-3: #7db8a8;
    --teal-4: #a8cfc5;
    --band-light: #a9cdc5;
    --band-dark: #5d8f88;
    --back-dark: #5a8586;
    --back-light: #bcd3d2;
    --white: #ffffff;
  }
  * { box-sizing: border-box; margin: 0; padding: 0; }
  html, body { width: 1200px; height: 755px; overflow: hidden; }
  body {
    background: var(--bg);
    font-family: "Barlow", Arial, sans-serif;
    display: flex;
    align-items: center;
    justify-content: center;
    gap: 40px;
  }
  .card {
    position: relative;
    width: 540px;
    height: 309px;
    border-radius: 3px;
    overflow: hidden;
  }

  /* Front */
  .card-front { background: var(--card-white); }
  .front-brand {
    position: absolute;
    top: 34px;
    right: 34px;
    display: flex;
    align-items: center;
    gap: 8px;
    color: var(--ink-teal);
    font-size: 14px;
    font-weight: 500;
    letter-spacing: 0.06em;
    text-transform: uppercase;
  }
  .brand-dot {
    width: 16px; height: 16px;
    border-radius: 50%;
    background: var(--ink-teal);
  }
  .contact-list {
    position: absolute;
    top: 92px;
    left: 0;
    list-style: none;
  }
  .contact-row {
    display: flex;
    align-items: center;
    height: 46px;
  }
  .contact-icon {
    width: 50px;
    height: 46px;
    display: flex;
    align-items: center;
    justify-content: center;
  }
  .contact-icon svg { width: 26px; height: 26px; }
  .row-name .contact-icon { background: var(--teal-1); }
  .row-tel .contact-icon { background: var(--teal-2); }
  .row-mail .contact-icon { background: var(--teal-3); }
  .row-web .contact-icon { background: var(--teal-4); }
  .contact-text {
    padding-left: 16px;
    color: var(--ink-teal);
  }
  .row-name .contact-text { font-size: 22px; align-self: flex-start; padding-top: 8px; }
  .row-tel .contact-text { font-size: 18px; }
  .row-mail .contact-text { font-size: 13px; }
  .row-web .contact-text { font-size: 14px; }
  .front-band-light {
    position: absolute;
    left: 0; right: 0;
    bottom: 22px;
    height: 12px;
    background: var(--band-light);
  }
  .front-band-dark {
    position: absolute;
    left: 0; right: 0;
    bottom: 0;
    height: 22px;
    background: var(--band-dark);
  }

  /* Back */
  .card-back {
    background: linear-gradient(210deg, var(--back-light) 0%, #8fb2b1 40%, var(--back-dark) 100%);
    color: var(--white);
  }
  .back-brand {
    position: absolute;
    top: 92px;
    left: 0; right: 0;
    display: flex;
    flex-direction: column;
    align-items: center;
    gap: 14px;
  }
  .back-brand .brand-dot {
    width: 44px; height: 44px;
    background: var(--white);
  }
  .back-brand-name {
    font-size: 26px;
    font-weight: 500;
    letter-spacing: 0.06em;
    text-transform: uppercase;
  }
  .back-web {
    position: absolute;
    bottom: 38px;
    left: 0; right: 0;
    text-align: center;
    font-size: 16px;
  }
</style>
</head>
<body>

  <section class="card card-front" aria-label="Business card front">
    <div class="front-brand"><span class="brand-dot"></span>The Brightwater Compass</div>

    <ul class="contact-list">
      <li class="contact-row row-name">
        <span class="contact-icon">
          <svg viewBox="0 0 24 24" fill="#ffffff" aria-hidden="true">
            <circle cx="12" cy="8" r="4.5"/>
            <path d="M3 22c0-5 4-8 9-8s9 3 9 8z"/>
          </svg>
        </span>
        <span class="contact-text">Corinne Fabrelle</span>
      </li>
      <li class="contact-row row-tel">
        <span class="contact-icon">
          <svg viewBox="0 0 24 24" fill="#ffffff" aria-hidden="true">
            <path d="M6.6 10.8a15 15 0 0 0 6.6 6.6l2.2-2.2c.3-.3.7-.4 1-.2 1.1.4 2.3.6 3.6.6.6 0 1 .4 1 1V20c0 .6-.4 1-1 1C10.6 21 3 13.4 3 4c0-.6.4-1 1-1h3.5c.6 0 1 .4 1 1 0 1.3.2 2.5.6 3.6.1.3 0 .7-.2 1z"/>
          </svg>
        </span>
        <span class="contact-text">TEL: +34 612 98 70 31</span>
      </li>
      <li class="contact-row row-mail">
        <span class="contact-icon">
          <svg viewBox="0 0 24 24" fill="none" stroke="#ffffff" stroke-width="1.8" aria-hidden="true">
            <rect x="3" y="6" width="18" height="13" rx="1" fill="#ffffff" stroke="none"/>
            <path d="M3 6l9 7 9-7" stroke="#7db8a8"/>
          </svg>
        </span>
        <span class="contact-text">corinne.fabrelle@thebrightwatercompass-mail.net</span>
      </li>
      <li class="contact-row row-web">
        <span class="contact-icon">
          <svg viewBox="0 0 24 24" fill="none" stroke="#ffffff" stroke-width="1.6" aria-hidden="true">
            <circle cx="12" cy="12" r="9"/>
            <ellipse cx="12" cy="12" rx="4" ry="9"/>
            <path d="M3 12h18M5 7h14M5 17h14"/>
          </svg>
        </span>
        <span class="contact-text">www.thebrightwatercompass-mail.net</span>
      </li>
    </ul>

    <div class="front-band-light"></div>
    <div class="front-band-dark"></div>
  </section>

  <section class="card card-back" aria-label="Business card back">
    <div class="back-brand">
      <span class="brand-dot"></span>
      <span class="back-brand-name">The Brightwater Compass</span>
    </div>
    <p class="back-web">www.thebrightwatercompass-mail.net</p>
  </section>

</body>
</html>
```